Anzeigengestaltung für Zahnarztpraxis
Zielgruppe
Wir sind eine Zahnarztpraxis in einer ländlichen Gemeinde mit 5000 Einwohnern in der Schweiz und bieten alles, was eine moderne Zahnarztpraxis zu bieten hat: Kieferorthopädie, allgemeine Zahnmedizin, Implantologie (schablonengeführt und digital geplant, Clarodent, Intraoralscanner, 3D-Röntgen
Online-Agenda
Zielgruppe: 4-99
2023: 20 jähriges Jubiläum
Der Text sollte später leicht und von uns selbständig geändert werden können:
z.B.
Frühjahrsputz: 20 Franken Rabatt auf die nächste Prophylaxesitzung
Aktion im April: 20% Rabatt auf Clarodent
Aktion im Mai 20% Rabatt auf Implantatbehandlungen
Sommeraktion Bleaching 495.-
Aufgabenstellung
Maße: 185x63mm, (185x130) beide quer
druckoptimiertes PDF X/-4
Bildauflösung: CMYK- und Graustufenbilder 300dpi
Farbprofil: PSOuncoated v3

```html
<!DOCTYPE html>
<html lang="de">
<head>
<meta charset="utf-8">
<title>Praxis Lindmann Zahnärzte – Jubiläumsanzeigen</title>
<link rel="stylesheet" href="https://fonts.googleapis.com/css2?family=Ubuntu:wght@300;400;500;700&display=swap">
<style>
  :root {
    --green-dark: #79b61a;
    --green-band: #93c43f;
    --grey: #737373;
    --grey-text: #6a6a6a;
    --white: #ffffff;
    --page: #ffffff;
    --frame: #3a3a3a;
  }
  * { margin: 0; padding: 0; box-sizing: border-box; }
  html, body {
    width: 1010px; height: 1200px; overflow: hidden;
    background: var(--page);
    font-family: "Ubuntu", sans-serif;
  }
  .sheet { position: relative; width: 1010px; height: 1200px; }
  .ad {
    position: absolute; left: 136px;
    width: 748px;
    border: 1px solid var(--frame);
    background: var(--white);
    box-shadow: 0 14px 28px rgba(0,0,0,0.16);
    overflow: hidden;
  }
  .ad--large { top: 141px; height: 526px; }
  .ad--banner { top: 784px; height: 255px; }
  .ad svg { display: block; }
  .brand-name { font-weight: 500; fill: var(--green-dark); }
  .brand-sub { font-weight: 400; fill: var(--grey-text); }
  .brand-dot { fill: var(--green-dark); }
  .headline { font-weight: 700; fill: var(--green-dark); }
  .url { font-weight: 500; fill: var(--grey-text); }
  .digit-two { font-weight: 700; fill: var(--green-dark); }
  .ring-grey { fill: var(--grey); fill-rule: evenodd; }
  .ring-green { fill: var(--green-dark); fill-rule: evenodd; }
  .years-label { font-weight: 300; fill: var(--grey); }
  .offer { font-weight: 500; fill: var(--white); }
  .badge-number { font-weight: 700; fill: var(--white); }
  .badge-percent { font-weight: 300; fill: var(--white); }
  .badge-label { font-weight: 700; fill: var(--white); letter-spacing: 4px; }
  .badge-ring { fill: none; stroke: var(--white); stroke-width: 1; }
  .badge-dots { fill: none; stroke: var(--white); stroke-width: 1.6; stroke-dasharray: 0.1 4; stroke-linecap: round; }
  .band { fill: var(--green-band); }
</style>
</head>
<body>
<div class="sheet">

  <!-- Large format ad -->
  <section class="ad ad--large">
    <svg width="748" height="526" viewBox="0 0 748 526" xmlns="http://www.w3.org/2000/svg">
      <defs>
        <clipPath id="ringLeftL"><rect x="520" y="80" width="95" height="260"/></clipPath>
        <clipPath id="ringRightL"><rect x="623" y="80" width="120" height="260"/></clipPath>
        <radialGradient id="visualGlowL" cx="50%" cy="45%" r="55%">
          <stop offset="0%" stop-color="#f4f4f4"/>
          <stop offset="75%" stop-color="#e6e6e6" stop-opacity="0.7"/>
          <stop offset="100%" stop-color="#e6e6e6" stop-opacity="0"/>
        </radialGradient>
      </defs>

      <circle class="brand-dot" cx="71" cy="73" r="33"/>
      <text class="brand-name" x="117" y="69" font-size="31">Praxis Lindmann</text>
      <text class="brand-sub" x="117" y="103" font-size="31">Zahnärzte</text>

      <text class="headline" font-size="56">
        <tspan x="50" y="189">Wir feiern</tspan>
        <tspan x="50" y="244">unser</tspan>
        <tspan x="50" y="298">Jubiläum!</tspan>
      </text>

      <text class="url" x="722" y="33" font-size="13" text-anchor="end">www.praxislindmann.ch</text>

      <rect role="img" aria-label="Weisser herzförmiger Ballon und Zahnimplantat mit Krone, umgeben von goldenem Sternkonfetti"
            x="335" y="10" width="220" height="345" rx="110" fill="url(#visualGlowL)"/>

      <rect class="band" x="0" y="356" width="748" height="170"/>

      <text class="digit-two" x="364" y="319" font-size="326" textLength="149" lengthAdjust="spacingAndGlyphs">2</text>
      <path class="ring-grey" clip-path="url(#ringLeftL)"
            d="M530 207a89 115.5 0 1 0 178 0a89 115.5 0 1 0 -178 0Z M566.5 208a49.5 81 0 1 0 99 0a49.5 81 0 1 0 -99 0Z"/>
      <path class="ring-green" clip-path="url(#ringRightL)"
            d="M530 207a89 115.5 0 1 0 178 0a89 115.5 0 1 0 -178 0Z M566.5 208a49.5 81 0 1 0 99 0a49.5 81 0 1 0 -99 0Z"/>
      <text class="years-label" x="616" y="217" font-size="28" text-anchor="middle">Jahre</text>

      <circle class="badge-ring" cx="200" cy="485" r="114"/>
      <circle class="badge-dots" cx="200" cy="485" r="102"/>
      <text class="badge-number" x="200" y="465" font-size="80" text-anchor="middle">20</text>
      <text class="badge-percent" x="200" y="484" font-size="22" text-anchor="middle">%</text>
      <text class="badge-label" x="202" y="508" font-size="16" text-anchor="middle">RABATT</text>

      <text class="offer" x="344" y="430" font-size="27">FEIERN &amp; SPAREN IM MAI –</text>
      <text class="offer" x="344" y="468" font-size="32">20 % AUF IMPLANTAT-</text>
      <text class="offer" x="344" y="505" font-size="32">BEHANDLUNGEN</text>
    </svg>
  </section>

  <!-- Banner format ad -->
  <section class="ad ad--banner">
    <svg width="748" height="255" viewBox="0 0 748 255" xmlns="http://www.w3.org/2000/svg">
      <defs>
        <clipPath id="ringLeftB"><rect x="360" y="50" width="59.6" height="180"/></clipPath>
        <clipPath id="ringRightB"><rect x="424.8" y="50" width="80" height="180"/></clipPath>
        <radialGradient id="visualGlowB" cx="50%" cy="45%" r="55%">
          <stop offset="0%" stop-color="#f4f4f4"/>
          <stop offset="75%" stop-color="#e6e6e6" stop-opacity="0.7"/>
          <stop offset="100%" stop-color="#e6e6e6" stop-opacity="0"/>
        </radialGradient>
      </defs>

      <rect class="band" x="465" y="0" width="283" height="255"/>

      <circle class="brand-dot" cx="46" cy="47" r="23"/>
      <text class="brand-name" x="79" y="42" font-size="21">Praxis Lindmann</text>
      <text class="brand-sub" x="79" y="66" font-size="21">Zahnärzte</text>

      <text class="headline" font-size="40">
        <tspan x="25" y="137">Wir feiern</tspan>
        <tspan x="25" y="177">unser</tspan>
        <tspan x="25" y="217">Jubiläum!</tspan>
      </text>

      <rect role="img" aria-label="Weisser herzförmiger Ballon und Zahnimplantat mit Krone, umgeben von goldenem Sternkonfetti"
            x="246" y="11" width="130" height="225" rx="65" fill="url(#visualGlowB)"/>

      <text class="digit-two" x="257" y="210" font-size="211" textLength="95" lengthAdjust="spacingAndGlyphs">2</text>
      <path class="ring-grey" clip-path="url(#ringLeftB)"
            d="M364 139a57.5 75 0 1 0 115 0a57.5 75 0 1 0 -115 0Z M389 140a33 53 0 1 0 66 0a33 53 0 1 0 -66 0Z"/>
      <path class="ring-green" clip-path="url(#ringRightB)"
            d="M364 139a57.5 75 0 1 0 115 0a57.5 75 0 1 0 -115 0Z M389 140a33 53 0 1 0 66 0a33 53 0 1 0 -66 0Z"/>
      <text class="years-label" x="421" y="146" font-size="17" text-anchor="middle">Jahre</text>

      <text class="url" x="406" y="236" font-size="10" text-anchor="middle">www.praxislindmann.ch</text>

      <text class="offer" x="607" y="37" font-size="18" text-anchor="middle">FEIERN &amp; SPAREN IM MAI –</text>
      <text class="offer" x="607" y="66" font-size="25" text-anchor="middle">20 % AUF IMPLANTAT-</text>
      <text class="offer" x="607" y="94" font-size="25" text-anchor="middle">BEHANDLUNGEN</text>

      <circle class="badge-ring" cx="607" cy="214" r="114"/>
      <circle class="badge-dots" cx="607" cy="214" r="102"/>
      <text class="badge-number" x="607" y="199" font-size="80" text-anchor="middle">20</text>
      <text class="badge-percent" x="607" y="222" font-size="21" text-anchor="middle">%</text>
      <text class="badge-label" x="609" y="241" font-size="15" text-anchor="middle">RABATT</text>
    </svg>
  </section>

</div>
</body>
</html>
```